online jewellery store business card

all black business card, glossy, with gold writing, gold logo and name (provided). simple design.

Target Market(s)

This business card is to put with purchases, so it just needs the logo and name Velmora Jewellery which I have uploaded pictures for you to use. Then it needs the web address, bidlorn address, email address and then the like us on KL for 10% off. All words to be used have been provided. Thanks

Industry/Entity Type

Store

Contact Information for Business Card

www.velmorajewellery.com
stores.bidlorn.com.au/Velmora-Jewellery
info@velmorajewellery.com

Like us on kinloop for 10% off your next purchase!

Requirements
Must have
• black background
gold writing
glossy look
Should not have
• yellow writing

```html
<!DOCTYPE html>
<html lang="en">
<head>
<meta charset="utf-8">
<title>Velmora Jewellery – Business Card</title>
<link rel="stylesheet" href="https://fonts.googleapis.com/css2?family=Ubuntu:wght@400;500&display=swap">
<style>
  :root {
    --backdrop: #3a302c;
    --card-black: #0b0b0b;
    --card-sheen: #1e1e1e;
    --gold: #c9a35a;
    --gold-soft: #b38e4c;
  }
  * { box-sizing: border-box; margin: 0; padding: 0; }
  html, body {
    width: 1200px;
    height: 716px;
    overflow: hidden;
    background: var(--backdrop);
  }
  .canvas {
    position: relative;
    width: 1200px;
    height: 716px;
    display: flex;
    align-items: center;
    justify-content: center;
    gap: 60px;
    font-family: "Ubuntu", sans-serif;
    color: var(--gold);
  }
  .card {
    position: relative;
    width: 520px;
    height: 298px;
    border-radius: 4px;
    background:
      linear-gradient(125deg, rgba(255,255,255,0.07) 0%, rgba(255,255,255,0) 38%, rgba(255,255,255,0) 62%, rgba(255,255,255,0.05) 100%),
      linear-gradient(180deg, var(--card-sheen) 0%, var(--card-black) 55%);
    box-shadow: 0 18px 40px rgba(0,0,0,0.45);
    overflow: hidden;
  }
  /* Front */
  .card-front {
    display: flex;
    flex-direction: column;
    align-items: center;
    justify-content: center;
    gap: 18px;
  }
  .brand-mark {
    display: block;
    width: 70px;
    height: 70px;
  }
  .brand-name {
    font-size: 30px;
    font-weight: 400;
    letter-spacing: 0.28em;
    line-height: 1.2;
    text-align: center;
    text-transform: uppercase;
    padding-left: 0.28em;
  }
  /* Back */
  .card-back {
    display: flex;
    flex-direction: column;
    align-items: center;
    justify-content: center;
    padding: 0 26px;
    text-align: center;
  }
  .back-mark {
    display: flex;
    align-items: center;
    gap: 10px;
    margin-bottom: 14px;
  }
  .back-mark svg { width: 44px; height: 44px; }
  .back-mark-name {
    font-size: 15px;
    letter-spacing: 0.24em;
    text-transform: uppercase;
  }
  .contact-list {
    list-style: none;
    font-size: 20px;
    font-weight: 500;
    line-height: 1.32;
  }
  .promo {
    margin-top: 12px;
    font-size: 13px;
    color: var(--gold-soft);
  }
</style>
</head>
<body>
  <main class="canvas">
    <section class="card card-front" aria-label="Business card front">
      <svg class="brand-mark" viewBox="0 0 70 70" aria-hidden="true">
        <circle cx="35" cy="35" r="32" fill="none" stroke="var(--gold)" stroke-width="2"/>
      </svg>
      <h1 class="brand-name">Velmora<br>Jewellery</h1>
    </section>

    <section class="card card-back" aria-label="Business card back">
      <div class="back-mark">
        <svg viewBox="0 0 44 44" aria-hidden="true">
          <circle cx="22" cy="22" r="20" fill="none" stroke="var(--gold)" stroke-width="1.6"/>
        </svg>
        <span class="back-mark-name">Velmora</span>
      </div>
      <ul class="contact-list">
        <li>www.velmorajewellery.com</li>
        <li>stores.bidlorn.com.au/Velmora-Jewellery</li>
        <li>info@velmorajewellery.com</li>
      </ul>
      <p class="promo">Like us on kinloop for 10% off your next purchase!</p>
    </section>
  </main>
</body>
</html>
```